Business Card Design

We need a business card design for a new dental practice in Brisbane. I'd like the basic details and logo on one side and appointment schedule on the other side. It is based in CBD office area and would prefer a professional and modern design.
Target Market(s)
20-60 years old office workers and residents with high education levels
Industry/Entity Type
Dental
Contact Information for Business Card
Harbourlight Dental
Dr Marcus Lindqvist
Principal Dentist
07 3194 6627
admin@harbourlightdentistry.example.au
www.harbourlightdentistry.example.au
S27, Level 3, Ferndale North Tower, 318 Gorrick St, Alderwood Heights, QLD 4118

```html
<!DOCTYPE html>
<html lang="en">
<head>
<meta charset="utf-8">
<title>Harbourlight Dental – Business Card</title>
<link rel="stylesheet" href="https://fonts.googleapis.com/css2?family=Quicksand:wght@400;500;600;700&display=swap">
<style>
  :root {
    --backdrop: #a3a5a6;
    --card: #ffffff;
    --brand-blue: #0a56a6;
    --ink: #1d2a3a;
    --muted-white: #dbe6f3;
  }
  * { box-sizing: border-box; margin: 0; padding: 0; }
  html, body {
    width: 1200px; height: 900px; overflow: hidden;
    background: var(--backdrop);
    font-family: "Quicksand", sans-serif;
  }
  .canvas {
    position: relative; width: 1200px; height: 900px;
    display: flex; align-items: center; justify-content: center; gap: 40px;
  }
  .card {
    position: relative; width: 500px; height: 306px;
    background: var(--card); overflow: hidden;
    box-shadow: 0 10px 24px rgba(0,0,0,0.18);
  }
  .block { position: absolute; background: var(--brand-blue); }

  /* Front */
  .front .block-top { top: 0; right: 0; width: 128px; height: 70px; }
  .front .block-bottom { bottom: 0; left: 0; width: 138px; height: 78px; }
  .brand {
    position: absolute; left: 0; right: 0; top: 128px;
    display: flex; align-items: center; justify-content: center; gap: 12px;
  }
  .brand-dot {
    width: 26px; height: 26px; border-radius: 50%; background: var(--brand-blue);
  }
  .brand-name {
    font-size: 30px; font-weight: 500; color: var(--ink); letter-spacing: 0.2px;
  }

  /* Back */
  .back .block-top { top: 0; right: 0; width: 100px; height: 22px; }
  .back .block-person {
    bottom: 0; left: 0; width: 196px; height: 122px;
    padding: 26px 16px 0 20px; color: #fff;
  }
  .person-name { font-size: 15px; font-weight: 700; text-transform: uppercase; letter-spacing: 0.3px; }
  .person-role { font-size: 11px; font-weight: 500; text-transform: uppercase; color: var(--muted-white); margin-top: 3px; letter-spacing: 0.4px; }
  .person-phone { display: flex; align-items: center; gap: 7px; font-size: 14px; font-weight: 500; margin-top: 8px; }
  .person-phone .icon circle { fill: #fff; }
  .person-phone .icon path { stroke: var(--brand-blue); }

  .contact-list {
    position: absolute; left: 210px; top: 104px; right: 14px;
    list-style: none; color: var(--brand-blue);
    font-size: 11.5px; font-weight: 500; line-height: 1.4;
  }
  .contact-item { display: flex; align-items: flex-start; gap: 8px; margin-bottom: 9px; }
  .icon { flex: 0 0 14px; width: 14px; height: 14px; margin-top: 1px; }
  .icon circle { fill: var(--brand-blue); }
  .icon path { stroke: #fff; fill: none; stroke-width: 1.3; stroke-linecap: round; stroke-linejoin: round; }
</style>
</head>
<body>
<main class="canvas">

  <section class="card front" aria-label="Card front">
    <div class="block block-top"></div>
    <div class="brand">
      <span class="brand-dot"></span>
      <span class="brand-name">Harbourlight Dental</span>
    </div>
    <div class="block block-bottom"></div>
  </section>

  <section class="card back" aria-label="Card back">
    <div class="block block-top"></div>

    <ul class="contact-list">
      <li class="contact-item">
        <svg class="icon" viewBox="0 0 14 14"><circle cx="7" cy="7" r="7"/><path d="M7 10.5 C5 8 4.6 7 4.6 6 a2.4 2.4 0 0 1 4.8 0 c0 1 -.4 2 -2.4 4.5z"/></svg>
        <span>S27, Level 3, Ferndale North Tower,<br>318 Gorrick St, Alderwood Heights,<br>QLD 4118</span>
      </li>
      <li class="contact-item">
        <svg class="icon" viewBox="0 0 14 14"><circle cx="7" cy="7" r="7"/><path d="M3.5 7 h7 M7 3.5 c-2 2 -2 5 0 7 c2 -2 2 -5 0 -7z"/></svg>
        <span>www.harbourlightdentistry.example.au</span>
      </li>
      <li class="contact-item">
        <svg class="icon" viewBox="0 0 14 14"><circle cx="7" cy="7" r="7"/><path d="M3.8 5 h6.4 v4.4 h-6.4z M3.8 5 l3.2 2.4 l3.2 -2.4"/></svg>
        <span>admin@harbourlightdentistry.example.au</span>
      </li>
    </ul>

    <div class="block block-person">
      <p class="person-name">Dr Marcus Lindqvist</p>
      <p class="person-role">Principal Dentist</p>
      <p class="person-phone">
        <svg class="icon" viewBox="0 0 14 14"><circle cx="7" cy="7" r="7"/><path d="M4.6 4 l1.4 0 l.6 1.6 l-.9 .7 c.5 1 1.1 1.6 2 2 l.7 -.9 l1.6 .6 l0 1.4 c-3 .3 -5.7 -2.4 -5.4 -5.4z"/></svg>
        <span>07 3194 6627</span>
      </p>
    </div>
  </section>

</main>
</body>
</html>
```